Flyer Design Dental Office Grand Opening offer

Dental office.

Grand opening flyer. Offer Exam + cleaning + xrays.
special: free teeth whitening ($200 value)

Target Market(s)

Middle class people around Huntington Beach.

Industry/Entity Type

Dental Clinic

Colors
cfeae6
86cfc6
fac994
fee18a
e667a6

Requirements
Must have
• Do not change my existing logo
Nice to have
• Have some appealing picture/design to catch the eye, but not too flashy
Should not have
• No cartoon kind of design

```html
<!DOCTYPE html>
<html lang="en">
<head>
<meta charset="utf-8">
<title>Harbor Dental – Grand Opening</title>
<link href="https://fonts.googleapis.com/css2?family=Anton&family=Roboto:wght@400;500&family=Roboto+Condensed:wght@700&display=swap" rel="stylesheet">
<style>
  :root {
    --teal: #0a9bb1;
    --teal-light: #8fd0da;
    --teal-pale: #c9e9ee;
    --orange: #f26522;
    --orange-soft: #f79a6b;
    --ink: #222222;
    --white: #ffffff;
    --backdrop: #e8e8e6;
  }
  html, body {
    margin: 0;
    width: 1044px;
    height: 1200px;
    overflow: hidden;
    background: var(--backdrop);
  }
  .flyer {
    position: absolute;
    left: 67px;
    top: 15px;
    width: 875px;
    height: 1124px;
    background: var(--white);
    transform: scale(1.04);
    transform-origin: top left;
    overflow: hidden;
    font-family: "Roboto", Arial, sans-serif;
    box-shadow: 0 6px 18px rgba(0,0,0,0.18);
  }
  .flyer-shapes { position: absolute; inset: 0; }
  .brand {
    position: absolute;
    right: 30px;
    top: 36px;
    text-align: right;
  }
  .brand-name {
    display: flex;
    align-items: center;
    gap: 12px;
    color: var(--teal);
    font-weight: 500;
    font-size: 44px;
    line-height: 1;
  }
  .brand-mark {
    width: 34px;
    height: 34px;
    background: var(--orange);
  }
  .brand-doctor {
    margin-top: 14px;
    font-size: 16px;
    color: var(--ink);
  }
  .headline {
    position: absolute;
    left: 50px;
    top: 728px;
    margin: 0;
    font-family: "Anton", Impact, sans-serif;
    font-weight: 400;
    color: var(--orange);
    font-size: 92px;
    line-height: 116px;
    letter-spacing: 1px;
  }
  .offers {
    position: absolute;
    left: 392px;
    top: 652px;
    width: 448px;
  }
  .offer {
    display: flex;
    align-items: center;
    border-bottom: 2px dotted #9a9a9a;
  }
  .offer-value {
    font-family: "Anton", Impact, sans-serif;
    color: var(--teal);
    font-size: 86px;
    line-height: 1;
    width: 180px;
  }
  .offer-text {
    color: var(--orange);
    font-size: 30px;
    line-height: 38px;
  }
  .offer-note { font-size: 16px; }
  .offer--exam { height: 118px; }
  .offer--whitening { height: 132px; }
  .offer-text--whitening small {
    display: block;
    font-size: 16px;
    line-height: 26px;
  }
  .insurance {
    display: flex;
    align-items: baseline;
    gap: 14px;
    margin-top: 12px;
  }
  .insurance-label {
    font-family: "Roboto Condensed", "Arial Narrow", sans-serif;
    font-weight: 700;
    color: var(--teal);
    font-size: 52px;
    letter-spacing: -1px;
  }
  .insurance-plans {
    color: var(--orange);
    font-size: 27px;
  }
  .contact {
    position: absolute;
    left: 48px;
    right: 36px;
    top: 1052px;
    display: flex;
    align-items: center;
    color: var(--white);
  }
  .contact-phone {
    display: flex;
    align-items: center;
    gap: 14px;
    font-family: "Roboto Condensed", "Arial Narrow", sans-serif;
    font-weight: 700;
    font-size: 38px;
  }
  .contact-address {
    margin-left: auto;
    display: flex;
    align-items: center;
    gap: 10px;
    font-size: 21px;
  }
</style>
</head>
<body>
<div class="flyer">
  <svg class="flyer-shapes" viewBox="0 0 875 1124" width="875" height="1124">
    <defs>
      <linearGradient id="photoTone" x1="0" y1="0" x2="1" y2="1">
        <stop offset="0" stop-color="#6f8f5e"/>
        <stop offset="0.3" stop-color="#c9a48c"/>
        <stop offset="0.6" stop-color="#e6d0c2"/>
        <stop offset="1" stop-color="#cfdcec"/>
      </linearGradient>
      <radialGradient id="mapTone" cx="0.5" cy="0.5" r="0.6">
        <stop offset="0" stop-color="#e4e4e4"/>
        <stop offset="1" stop-color="#cfd2cf"/>
      </radialGradient>
    </defs>
    <path class="family-photo" role="img" aria-label="Photo of a smiling family of four huddled together outdoors"
          fill="url(#photoTone)"
          d="M0,0 L345,0 C365,120 470,220 875,222 L875,595 C700,590 500,580 330,560 C200,545 80,505 0,470 Z"/>
    <path class="photo-edge" fill="none" stroke="var(--teal-light)" stroke-width="9"
          d="M349,-4 C369,116 474,216 879,218"/>
    <path class="wave-band" fill="var(--teal)"
          d="M0,470 C80,505 200,545 330,560 C500,580 700,590 875,595 L875,615 C700,612 520,605 350,590 C220,575 100,540 0,505 Z"/>
    <circle class="map-ring" cx="195" cy="560" r="146" fill="var(--teal-pale)"/>
    <circle class="location-map" role="img" aria-label="Street map showing the office location" cx="195" cy="560" r="125" fill="url(#mapTone)"/>
    <path class="footer-band" fill="var(--teal)"
          d="M0,963 C250,1032 600,1030 875,985 L875,1124 L0,1124 Z"/>
    <path class="footer-accent" fill="var(--orange-soft)"
          d="M520,1020 C660,1012 780,1000 875,980 L875,1004 C780,1016 660,1022 520,1020 Z"/>
  </svg>

  <div class="brand">
    <div class="brand-name"><span class="brand-mark"></span>Harbor Dental</div>
    <div class="brand-doctor">Linh Tran, DDS</div>
  </div>

  <h1 class="headline">GRAND<br>OPENING</h1>

  <div class="offers">
    <div class="offer offer--exam">
      <div class="offer-value">$50</div>
      <div class="offer-text">Exam with Xrays &amp;<br>Cleaning <span class="offer-note">(regular)</span></div>
    </div>
    <div class="offer offer--whitening">
      <div class="offer-value">FREE</div>
      <div class="offer-text offer-text--whitening">BLEACHING<small>(after completion of dental treatment)</small></div>
    </div>
    <div class="insurance">
      <span class="insurance-label">welcomed</span>
      <span class="insurance-plans">PPO, HMO, MediDent</span>
    </div>
  </div>

  <div class="contact">
    <div class="contact-phone">
      <svg width="38" height="38" viewBox="0 0 38 38" aria-hidden="true">
        <circle cx="19" cy="19" r="16.5" fill="none" stroke="#fff" stroke-width="3"/>
        <path fill="#fff" d="M13.5,10.5 l3.2,-0.6 l2,5 l-2.3,1.7 c1,2.4 2.6,4 5,5 l1.7,-2.3 l5,2 l-0.6,3.2 c-9,0.6 -14.6,-5 -14,-14 z"/>
      </svg>
      <span>(714) 555-0182</span>
    </div>
    <div class="contact-address">
      <svg width="14" height="20" viewBox="0 0 14 20" aria-hidden="true">
        <path fill="#fff" d="M7,0 C3,0 0,3 0,7 C0,12 7,20 7,20 C7,20 14,12 14,7 C14,3 11,0 7,0 Z M7,10 A3,3 0 1 1 7,4 A3,3 0 1 1 7,10 Z"/>
      </svg>
      <span>2280 Seacliff Ave., Coastline City, CA 90000</span>
    </div>
  </div>
</div>
</body>
</html>
```